Banner for Vet Hospital 5m x 1.2m - Heat Stroke

Maplecourt Pet Hospital needs a Heat Stroke Banner for Summer.
The banner will be 5000mm long and 1200mm tall.

Our region has been hot this year and this summer is going to be extremely hot.
I want to warn people about heat stroke.
I want you to create a heat stroke banner that conveys the symptoms of heat stroke.

Pictures are better than words.
There should be IMAGES and WORDS that can be seen from the road 30m away and maybe some smaller words for people to read as they walk past.

Here are some of the signs of Heat Stroke:
- Panting which increases as heatstroke progresses
- Drooling, salivating
- Agitation, restlessness
- Very red or pale gums
- Bright red tongue
- Increased heart rate
- Breathing distress
- Vomiting Diarrhea (possibly with blood)
- Signs of mental confusion, delirium
- Dizziness, staggering
- Lethargy, weakness
- Muscle tremors
- Seizures
- Collapsing and lying down
- Little to no urine production
- Coma

I have attached characters that we often use in our advertising. They are optional.
I have done a mock up of the design I imagine. You could refine this design or make your own....or both.

Target Market(s)

Women aged 20 to 50.

Industry/Entity Type

Veterinary

Font styles to use
Sans Serif

Colors
fbed22
f78f20
ec1f27
ffffff

Requirements
Must have
• Heat Stroke Symtpms.
• Heat Stroke Warning.
• Summer theme.
Nice to have
• Bright colours.

```html
<!DOCTYPE html>
<html lang="en">
<head>
<meta charset="UTF-8">
<title>Heat Stroke Symptoms Banner</title>
<link href="https://fonts.googleapis.com/css2?family=Anton&family=Roboto+Condensed:wght@500&display=swap" rel="stylesheet">
<style>
  :root {
    --yellow: #fbed22;
    --orange: #f78f20;
    --red: #ec1f27;
    --white: #ffffff;
    --sky-top: #5fa7de;
    --sky-bottom: #cfe6f5;
    --grass-top: #6fbf3a;
    --grass-bottom: #3f8f1f;
    --fawn: #d9c3a0;
    --cat: #e8a766;
    --dog: #9c8b7c;
  }
  * { margin: 0; padding: 0; box-sizing: border-box; }
  html, body { width: 1200px; height: 288px; overflow: hidden; background: var(--white); }
  .banner { position: relative; width: 1200px; height: 288px; overflow: hidden; }
  .scene {
    position: absolute; left: 0; top: 0; width: 1200px; height: 198px;
    background: linear-gradient(180deg, var(--sky-top) 0%, var(--sky-bottom) 42%, var(--grass-top) 58%, var(--grass-bottom) 100%);
  }
  .symptom-band { position: absolute; left: 0; top: 198px; width: 1200px; height: 90px; display: flex; }
  .symptom-group {
    height: 100%;
    font-family: "Roboto Condensed", "Arial Narrow", sans-serif;
    font-weight: 500; font-size: 13.5px; line-height: 17.4px;
    list-style: none; padding-top: 13px; text-transform: uppercase;
  }
  .symptom-group--yellow { background: var(--yellow); color: var(--red); }
  .symptom-group--orange { background: var(--orange); color: var(--white); }
  .group-1 { width: 222px; padding-left: 28px; }
  .group-2 { width: 353px; padding-left: 39px; }
  .group-3 { width: 300px; padding-left: 32px; }
  .group-4 { width: 325px; padding-left: 63px; }
  .title-art { position: absolute; left: 0; top: 0; width: 1200px; height: 198px; }
  .title-text { font-family: "Anton", "Impact", sans-serif; fill: var(--yellow); }
</style>
</head>
<body>
<main class="banner">
  <div class="scene" role="img" aria-label="Photo of blue summer sky over green grass"></div>

  <section class="symptom-band" aria-label="Heat stroke symptoms">
    <ul class="symptom-group symptom-group--yellow group-1">
      <li>Panting</li>
      <li>Drooling, salivating</li>
      <li>Agitation, restlessness</li>
      <li>Very red or pale gums</li>
    </ul>
    <ul class="symptom-group symptom-group--orange group-2">
      <li>Bright red tongue</li>
      <li>Increased heart rate</li>
      <li>Breathing distress</li>
      <li>Vomiting diarrhea (possibly with blood)</li>
    </ul>
    <ul class="symptom-group symptom-group--yellow group-3">
      <li>Signs of mental confusion, delirium</li>
      <li>Dizziness, staggering</li>
      <li>Lethargy, weakness</li>
      <li>Muscle tremors</li>
    </ul>
    <ul class="symptom-group symptom-group--orange group-4">
      <li>Seizures</li>
      <li>Collapsing and lying down</li>
      <li>Little to no urine production</li>
      <li>Coma</li>
    </ul>
  </section>

  <svg class="title-art" viewBox="0 0 1200 198" xmlns="http://www.w3.org/2000/svg">
    <rect x="35" y="6" width="124" height="190" rx="40" fill="var(--fawn)" role="img" aria-label="Photo of a sitting pug dog"/>
    <polygon points="209,74 936,13 936,96 209,144" fill="var(--red)"/>
    <polygon points="389,150 754,111 754,158 389,190" fill="var(--red)"/>
    <rect x="224" y="40" width="82" height="110" rx="28" fill="var(--cat)" role="img" aria-label="Illustration of an orange tabby cat"/>
    <rect x="850" y="7" width="56" height="84" rx="20" fill="var(--dog)" role="img" aria-label="Illustration of a panting brown dog"/>
    <rect x="880" y="66" width="291" height="140" rx="58" fill="var(--fawn)" role="img" aria-label="Photo of an exhausted pug lying down"/>
    <text class="title-text" x="579" y="104" font-size="62" text-anchor="middle" textLength="520" lengthAdjust="spacingAndGlyphs" transform="rotate(-4.8 579 82)">HEAT STROKE</text>
    <text class="title-text" x="571" y="165" font-size="40" text-anchor="middle" textLength="270" lengthAdjust="spacingAndGlyphs" transform="rotate(-5.5 571 151)">SYMPTOMS</text>
  </svg>
</main>
</body>
</html>
```